Media and Film Company Needs a New Website

We produce highly stylized commercials and film pieces for our clients. We also produce live events, both corporate and theatrical. Looking for a site that can show off our client videos - have a polished way to show off our team, and be able to create pages to highlight our clients and give a full overview of our project/process with them. We design simple website for some of our clients - so we are very wordpress familiar, and would like something that doesn't feel like a template.

Target Market(s)

content creators, creative directors, production teams, marketing agencies

Industry/Entity Type

Film Production

Number of Pages Required

4 page

Font styles to use
Sans Serif

Requirements
Must have
• slick looking video embed (from YT or Vimeo)
• project pages - client snapshot (what we did for them, how we did it)
• nice landing page, have our company video reel on the page
• testimonials
• contact page
• ability to have photos as a background if we want
Nice to have
• polished clean look - look to our logo colors and linear elements
• we produce very stylized videos for our clients and our website should reflect that
Should not have
• template look or feel to it- please bring your flare to the project!
• take a look at our current site - zantorvo.com we need a better way to highlight our work and our clients

```html
<!DOCTYPE html>
<html lang="en">
<head>
<meta charset="utf-8">
<title>About Us — Zantorvo Media &amp; Entertainment</title>
<link rel="stylesheet" href="https://fonts.googleapis.com/css2?family=Source+Sans+3:wght@300;400;600;700&display=swap">
<style>
:root{
  --black:#0b0b0b;
  --ink:#333333;
  --cyan:#1ab3e6;
  --white:#ffffff;
  --grey-band:#e9e9e9;
  --grey-text:#8a8a8a;
  --nav-text:#cfcfcf;
}
*{margin:0;padding:0;box-sizing:border-box}
html,body{width:720px;height:1200px;overflow:hidden}
body{font-family:"Source Sans 3",Arial,sans-serif;color:var(--ink);background:var(--white);position:relative}
.site-header{position:absolute;left:0;top:0;width:720px;height:72px;background:var(--black)}
.brand{position:absolute;left:88px;top:20px;display:flex;align-items:center;gap:8px;color:var(--white);font-weight:700;font-size:20px;letter-spacing:1px}
.brand-dot{width:14px;height:14px;border-radius:50%;background:var(--cyan)}
.brand small{display:block;font-size:9px;font-weight:700;letter-spacing:2px;color:var(--white)}
.main-nav{position:absolute;right:82px;top:30px;display:flex;gap:4px}
.main-nav a{font-size:10px;color:var(--nav-text);text-decoration:none;padding:3px 10px}
.main-nav a.active{background:var(--white);color:var(--cyan)}
.hero{position:absolute;left:0;top:72px;width:720px;height:242px;background:var(--white);overflow:hidden}
.hero-photo{position:absolute;left:0;top:0;width:440px;height:242px;background:linear-gradient(100deg,#050505 0%,#2b2b2b 38%,#6d6d6d 62%,#e6e6e6 90%,rgba(255,255,255,0) 100%)}
.hero-title{position:absolute;left:442px;top:104px;font-size:52px;font-weight:300;line-height:1;color:var(--cyan)}
.about{position:absolute;left:96px;top:360px;width:540px;font-size:11.5px;line-height:1.55}
.about p{margin-bottom:14px}
.clients{position:absolute;left:0;top:564px;width:720px;height:560px;background:var(--grey-band)}
.clients h2{position:absolute;left:0;top:36px;width:720px;text-align:center;font-size:36px;font-weight:300;color:var(--ink)}
.client-grid{position:absolute;left:96px;top:116px;width:540px;display:grid;grid-template-columns:repeat(4,1fr);row-gap:40px}
.client{display:flex;align-items:center;justify-content:center;gap:6px;height:40px;font-size:14px;font-weight:600;color:#3d4a5c;white-space:nowrap}
.client i{width:12px;height:12px;border-radius:50%;background:var(--cyan);display:block}
.client b{width:11px;height:11px;background:#c2452f;display:block}
.more-btn{position:absolute;left:288px;top:480px;width:144px;height:34px;background:var(--cyan);color:var(--white);font-size:12px;display:flex;align-items:center;justify-content:center}
.site-footer{position:absolute;left:0;top:1124px;width:720px;height:76px;background:var(--black)}
.cta{position:absolute;left:34px;top:22px;font-size:13px;color:var(--cyan)}
.social{position:absolute;right:50px;top:20px;display:flex;gap:8px}
.social span{width:18px;height:18px;border-radius:50%;background:#2f8fb0;display:block}
.copyright{position:absolute;left:0;top:56px;width:720px;text-align:center;font-size:8px;color:var(--grey-text);letter-spacing:.5px}
</style>
</head>
<body>
<header class="site-header">
  <div class="brand"><span class="brand-dot"></span><div>ZANTORVO<small>MEDIA &amp; ENTERTAINMENT</small></div></div>
  <nav class="main-nav">
    <a class="active" href="#">Home</a><a href="#">Portfolio</a><a href="#">About ZME</a><a href="#">Testimonials</a><a href="#">Press</a><a href="#">Contact Us</a>
  </nav>
</header>

<section class="hero">
  <div class="hero-photo" role="img" aria-label="Close-up of a professional video camera in dark tones"></div>
  <h1 class="hero-title">About Us</h1>
</section>

<section class="about">
  <p>Zantorvo Media &amp; Entertainment provides full service campaigns in film and media production, live entertainment &amp; theatrical production, marketing &amp; advertising, and event management in the DC metro area.</p>
  <p>Founded in 2009, Zantorvo Media &amp; Entertainment has built a reputation working for clients including the Meridian Screen Institute, Halden Leaders, Corwell Music, Riverbend Community Resources, and Brightvale Events.</p>
  <p>Zantorvo Media &amp; Entertainment works to build strong relationships with its clients through full service campaigns in multiple industries. Through community outreach, Zantorvo develops its campaigns thoroughly to provide the most successful services to its clients.</p>
</section>

<section class="clients">
  <h2>Our Clients</h2>
  <div class="client-grid">
    <div class="client">Oakroot Studio</div>
    <div class="client">Fistrel</div>
    <div class="client">Varden</div>
    <div class="client"><i></i>Norlia</div>
    <div class="client">Reelhouse Docs</div>
    <div class="client">Kestrel Fdn.</div>
    <div class="client"><i></i>tinyForge</div>
    <div class="client"><b></b>Brightvale</div>
    <div class="client">Halden</div>
    <div class="client">Saverna</div>
    <div class="client"><i></i>Riverbend CR</div>
    <div class="client">Orvia</div>
    <div class="client">Green Path</div>
    <div class="client">Corwell Music</div>
    <div class="client">Sentrell's</div>
    <div class="client">Prism Foods</div>
  </div>
  <a class="more-btn">and many more...</a>
</section>

<footer class="site-footer">
  <p class="cta">Ready to get to work?? Contact us today - info@zantorvo.com</p>
  <div class="social"><span></span><span></span><span></span><span></span><span></span></div>
  <p class="copyright">©2016 ZANTORVO MEDIA &amp; ENTERTAINMENT</p>
</footer>
</body>
</html>
```